Want a package created for a new protein bar

We would like a new package created for a new protein bar project The name of the bar will be VOLMBite a real food protein bar, we would like a ‘window’ on the package of bar like Brave Meadow bar below in images.

VOLMBite
‘Super Food Bar’
14g of Whey Protein
The package film size is the following 12cm width x 15cm Length,
Flavor Peanut Chocolate Chip, additional information will be attached shortly like nutrition facts,

Target Market(s)

fitness market, bodybuilders, athletes, everyday people

Industry/Entity Type

Health Product

Logo Text

VOLMBite

Font styles to use
Serif
Sans Serif
Decorative

Requirements
Must have
• Package window

```html
<!DOCTYPE html>
<html lang="en">
<head>
<meta charset="utf-8">
<title>VOLMBite Protein Bar Wrapper</title>
<link href="https://fonts.googleapis.com/css2?family=Montserrat:wght@400;600;800&display=swap" rel="stylesheet">
<style>
  :root {
    --bg-light: #c9da94;
    --bg-dark: #a9bc7c;
    --green-bright: #35a82e;
    --green-mid: #1f7a24;
    --green-deep: #0c4219;
    --band-white: #ffffff;
    --ink: #151815;
  }
  * { margin: 0; padding: 0; box-sizing: border-box; }
  html, body { width: 1200px; height: 800px; overflow: hidden; }
  body {
    position: relative;
    background: linear-gradient(160deg, var(--bg-dark) 0%, var(--bg-light) 55%, var(--bg-dark) 100%);
    font-family: "Montserrat", sans-serif;
  }
  .wrapper {
    position: absolute;
    left: 150px;
    top: 230px;
    width: 900px;
    height: 320px;
  }
  .wrapper-shape { position: absolute; inset: 0; }
  .brand-mark {
    position: absolute;
    left: 78px;
    top: 112px;
    width: 56px;
    height: 56px;
    border-radius: 50%;
    background: var(--green-mid);
  }
  .brand-name {
    position: absolute;
    left: 150px;
    top: 114px;
    font-size: 48px;
    font-weight: 600;
    letter-spacing: 5px;
    color: var(--ink);
    line-height: 1;
    white-space: nowrap;
  }
  .product-type {
    position: absolute;
    left: 548px;
    top: 106px;
    font-size: 9px;
    font-weight: 400;
    color: var(--ink);
    line-height: 1.4;
    letter-spacing: 0.5px;
  }
  .weight-box {
    position: absolute;
    left: 78px;
    top: 210px;
    width: 74px;
    height: 62px;
    border: 2px solid var(--band-white);
    border-radius: 4px;
    background: var(--green-deep);
    color: var(--band-white);
    font-size: 32px;
    font-weight: 400;
    display: flex;
    align-items: center;
    justify-content: center;
  }
  .flavour-line {
    position: absolute;
    left: 170px;
    top: 212px;
    font-size: 21px;
    font-weight: 800;
    letter-spacing: 1.5px;
    color: var(--band-white);
    white-space: nowrap;
  }
  .claim-line {
    position: absolute;
    left: 170px;
    top: 245px;
    font-size: 17px;
    font-weight: 400;
    letter-spacing: 3px;
    color: var(--band-white);
    white-space: nowrap;
  }
  .layer-badge {
    position: absolute;
    left: 600px;
    top: 0;
    width: 86px;
    height: 58px;
    background: var(--band-white);
    text-align: center;
    font-size: 11px;
    font-weight: 600;
    color: var(--ink);
    line-height: 1.25;
    padding-top: 6px;
  }
  .layer-badge::after {
    content: "";
    position: absolute;
    left: 8px;
    right: 8px;
    bottom: -14px;
    height: 14px;
    background: linear-gradient(90deg, var(--green-mid), var(--green-bright));
  }
  .corner-lockup {
    position: absolute;
    left: 875px;
    top: 690px;
    display: flex;
    align-items: center;
    gap: 12px;
  }
  .corner-lockup .lockup-mark {
    width: 34px;
    height: 34px;
    border-radius: 50%;
    background: var(--green-mid);
  }
  .corner-lockup .lockup-name {
    font-size: 34px;
    font-weight: 600;
    letter-spacing: 5px;
    color: #2a2d28;
  }
</style>
</head>
<body>
  <div class="wrapper">
    <svg class="wrapper-shape" width="900" height="320" viewBox="0 0 900 320">
      <defs>
        <linearGradient id="filmGreen" x1="0" y1="0" x2="0" y2="1">
          <stop offset="0" stop-color="#35a82e"/>
          <stop offset="0.55" stop-color="#1f7a24"/>
          <stop offset="1" stop-color="#0c4219"/>
        </linearGradient>
        <linearGradient id="windowFill" x1="0" y1="0" x2="1" y2="1">
          <stop offset="0" stop-color="#f2c35a"/>
          <stop offset="0.6" stop-color="#d18f33"/>
          <stop offset="1" stop-color="#7a4a22"/>
        </linearGradient>
      </defs>
      <polygon fill="url(#filmGreen)" points="52,0 12,0 0,10 12,20 0,30 12,40 0,50 12,60 0,70 12,80 0,90 12,100 0,110 12,120 0,130 12,140 0,150 12,160 0,170 12,180 0,190 12,200 0,210 12,220 0,230 12,240 0,250 12,260 0,270 12,280 0,290 12,300 0,310 12,320 52,320"/>
      <polygon fill="url(#filmGreen)" points="848,0 888,0 900,10 888,20 900,30 888,40 900,50 888,60 900,70 888,80 900,90 888,100 900,110 888,120 900,130 888,140 900,150 888,160 900,170 888,180 900,190 888,200 900,210 888,220 900,230 888,240 900,250 888,260 900,270 888,280 900,290 888,300 900,310 888,320 848,320"/>
      <rect x="50" y="0" width="800" height="320" fill="url(#filmGreen)"/>
      <polygon fill="#ffffff" points="0,90 12,100 0,110 12,120 0,130 12,140 0,150 12,160 0,170 12,180 0,190 600,190 600,90"/>
      <g stroke="#ffffff" stroke-opacity="0.25" stroke-width="2">
        <line x1="24" y1="0" x2="24" y2="320"/>
        <line x1="36" y1="0" x2="36" y2="320"/>
        <line x1="864" y1="0" x2="864" y2="320"/>
        <line x1="876" y1="0" x2="876" y2="320"/>
      </g>
      <rect x="600" y="0" width="215" height="320" fill="url(#windowFill)" role="img" aria-label="Window showing the granola protein bar with peanuts and chocolate chips"/>
      <rect x="815" y="0" width="35" height="320" fill="#0c4219"/>
    </svg>

    <div class="brand-mark"></div>
    <div class="brand-name">VOLMBITE</div>
    <div class="product-type">PROTEIN<br>BAR</div>

    <div class="weight-box">20g</div>
    <div class="flavour-line">PEANUT | CHOCOLATE | SUGAR</div>
    <div class="claim-line">100% NATURAL</div>

    <div class="layer-badge">DOUBLE<br>LAYER</div>
  </div>

  <div class="corner-lockup">
    <div class="lockup-mark"></div>
    <div class="lockup-name">VOLMBITE</div>
  </div>
</body>
</html>
```